Website for new dental office

I am Dr. Colin Marsh and am building a new dental practice. I specialize in general dentistry. I am young and have a higher end dental practice incorporating very new technologies and would like my website to reflect that. As many dental patients are older, the website must be very easy to navigate. I would like patients to be able to request appointments, and will eventually add on patient information forms (the health history, etc, that you normally fill out in the practice) from my practice management software, so leave an area for that.

Industry/Entity Type

Building

```html
<!DOCTYPE html>
<html lang="en">
<head>
<meta charset="utf-8">
<title>MarshSmile Dental – Dr. Colin Marsh</title>
<link href="https://fonts.googleapis.com/css2?family=Arimo:wght@400;700&family=Ubuntu:wght@300;400;500;700&family=Yanone+Kaffeesatz:wght@300;400;600;700&display=swap" rel="stylesheet">
<style>
:root{
  --blue:#3f7ac5;
  --blue-dark:#2f63ad;
  --gold:#c8961e;
  --ink:#333;
  --muted:#888;
  --page:#fbfbfb;
  --card1:#40a9e1;
  --card2:#1c84d3;
  --card3:#2f61b2;
  --card4:#2c3e98;
  --bar:#4b4b4b;
  --footer:#4a4a4a;
  --footer-text:#d6d6d6;
}
*{margin:0;padding:0;box-sizing:border-box}
html,body{width:1103px;height:1200px;overflow:hidden}
body{position:relative;background:var(--page);font-family:"Arimo",Arial,sans-serif;color:var(--ink)}
.abs{position:absolute}

/* header */
.social-top{left:667px;top:7px;font-size:9.5px;color:var(--muted);display:flex;gap:12px}
.brand{left:214px;top:16px;width:270px;height:80px;display:flex;align-items:center;gap:12px}
.brand-mark{width:64px;height:64px;border-radius:50%;background:linear-gradient(#eef3f8,#d5e0ea);flex:none}
.brand-name{font-family:"Ubuntu",sans-serif;font-size:20px;font-weight:500;color:var(--blue-dark);letter-spacing:-.2px}
.chat{left:644px;top:32px;width:128px;height:62px}
.chat-avatar{left:0;top:2px;width:44px;height:58px;border-radius:22px 22px 10px 22px;background:linear-gradient(#c9a382 0%,#e9d7c7 45%,#f2f2f2 100%)}
.chat-q{left:38px;top:7px;font-family:"Ubuntu",sans-serif;font-size:11.5px;color:var(--blue-dark);white-space:nowrap}
.chat-btn{left:50px;top:25px;width:82px;height:32px;border-radius:4px;background:linear-gradient(#edc04a,#c8961e);color:#fff;padding:4px 6px;white-space:nowrap}
.chat-btn small{display:block;font-size:7px;line-height:8px;color:#6b4a00}
.chat-btn span{font-family:"Ubuntu",sans-serif;font-size:13px;font-weight:300;line-height:16px}
.enquiries{left:780px;top:42px;border-left:1px solid #ddd;padding-left:10px;font-family:"Ubuntu",sans-serif;line-height:15px}
.enquiries h4{font-size:10px;color:var(--blue);font-weight:700;display:flex;gap:6px;align-items:center;margin-bottom:2px}
.enquiries p{font-size:12.5px;color:#222;white-space:nowrap}

.nav{left:214px;top:102px;width:676px;height:28px;background:linear-gradient(#4c87d2,#3a72bd);display:flex;border-radius:2px 2px 0 0}
.nav a{color:#fff;font-size:9px;text-decoration:none;padding:0 16px;line-height:28px;border-right:1px solid rgba(255,255,255,.25)}
.nav a.active{background:linear-gradient(#e4ad2e,#c8961e);color:#5a3b00;font-weight:700;padding:0 15px}

/* hero */
.hero{left:0;top:130px;width:1103px;height:307px;background:linear-gradient(90deg,#cfd8e0 0%,#e6ecf1 40%,#eef2f5 70%,#f6f7f8 100%)}
.hero-window{left:0;top:130px;width:478px;height:307px;background:
  linear-gradient(90deg,transparent 0 108px,rgba(255,255,255,.35) 108px 118px,transparent 118px 300px,rgba(170,185,200,.35) 300px 312px,transparent 312px),
  linear-gradient(180deg,rgba(255,255,255,.25),transparent 30%)}
.hero-photo{left:478px;top:130px;width:412px;height:254px;background:
  linear-gradient(90deg,rgba(230,236,241,1) 0%,rgba(230,236,241,0) 14%),
  linear-gradient(180deg,#eceae6 0%,#e2d2bb 38%,#dfb867 70%,#d9a234 100%)}
.hero-copy{left:214px;top:248px;font-family:"Ubuntu",sans-serif}
.hero-copy .lead{font-size:22px;font-weight:300;color:var(--blue-dark);line-height:22px}
.hero-copy .title{font-size:26px;font-weight:700;color:var(--gold);line-height:28px}
.hero-copy .sub{font-size:16px;font-weight:300;color:#444;letter-spacing:-.3px}

/* appointment */
.appt{left:214px;top:384px;width:676px;height:198px;background:var(--blue);color:#fff}
.tab{top:0;height:42px;font-family:"Yanone Kaffeesatz",sans-serif;font-size:21px;line-height:42px;padding-left:16px}
.tab.main{left:0;width:342px}
.tab.emergency{left:342px;width:334px;background:#fff;color:var(--blue);padding-left:20px;display:flex;gap:10px;align-items:center}
.col{top:62px}
.col h3{font-family:"Yanone Kaffeesatz",sans-serif;font-weight:400;font-size:18px;display:flex;gap:8px;align-items:center}
.hours{left:16px;width:194px}
.hours ul{list-style:none;margin-top:16px;font-size:9.5px}
.hours li{display:flex;justify-content:space-between;padding:0 4px;height:27px;align-items:center;border-bottom:1px solid rgba(255,255,255,.6)}
.hours li:last-child{border:0}
.timetable{left:216px;width:145px}
.timetable p{font-size:9px;line-height:11px;margin-top:18px}
.btn{position:absolute;background:#fff;color:var(--blue);font-size:9.5px;text-align:center;line-height:18px;height:18px}
.booking{left:380px;width:280px}
.field{position:absolute;width:121px;height:21px;border:1px solid #fff;font-size:9.5px;line-height:19px;padding-left:6px}

/* services */
.section-title{left:214px;top:620px;font-family:"Yanone Kaffeesatz",sans-serif;font-size:24px;color:#444;font-weight:300}
.section-title b{color:var(--gold);font-weight:700}
.section-rule{left:214px;top:650px;width:676px;height:1px;background:#e3e3e3}
.section-accent{left:258px;top:648px;width:80px;height:3px;background:var(--gold)}
.cards{left:214px;top:676px;display:flex;gap:3px}
.card{width:167px;height:232px;position:relative;color:#fff}
.card-photo{height:104px}
.card-photo.cosmetic{background:linear-gradient(100deg,#f3ece7 0%,#e9dcd3 35%,#c79a84 60%,#3b2a26 85%,#5a403a 100%)}
.card-photo.whiten{background:linear-gradient(180deg,#f2d9d2 0%,#e9b3ad 30%,#f5f2ee 50%,#d7505c 72%,#b8303f 100%)}
.card-photo.smile{background:linear-gradient(180deg,#e2bfb8 0%,#c85a5e 28%,#f4f0ea 45%,#e9e4dc 60%,#b6383f 80%,#8f2a33 100%)}
.card-photo.implant{background:linear-gradient(160deg,#f1f1f1 0%,#d9d9d9 40%,#b8b8b8 70%,#cfcfcf 100%)}
.card-body{height:106px;padding:10px 14px}
.card h4{font-family:"Yanone Kaffeesatz",sans-serif;font-size:22px;font-weight:300;line-height:24px}
.card h4 b{font-weight:700}
.card p{font-size:9px;line-height:14px;opacity:.85;margin-top:6px}
.card .more{height:22px;background:var(--bar);font-family:"Yanone Kaffeesatz",sans-serif;font-size:12px;line-height:22px;padding-left:15px}
.plus{position:absolute;right:0;top:92px;width:12px;height:12px;background:#3b3b3b}
.c1 .card-body{background:var(--card1)}
.c2 .card-body{background:var(--card2)}
.c3 .card-body{background:var(--card3)}
.c4 .card-body{background:var(--card4)}

/* partners */
.band{left:0;top:983px;width:1103px;height:83px;background:#f0f0f0}
.partners{left:214px;top:942px;width:676px;height:89px;background:#fff;border:1px solid #ececec;display:flex;align-items:center;justify-content:space-between;padding:0 13px}
.arrow{width:19px;height:19px;background:var(--blue);display:flex;align-items:center;justify-content:center}
.badge{width:112px;height:50px;display:flex;align-items:center;justify-content:center}
.badge i{display:block;width:44px;height:44px;border-radius:50%}
.badge.p1 i{background:#2f63ad;opacity:.85}
.badge.p2 i{background:#c9643a;opacity:.8}
.badge.p3 i{background:#1f9bb0;opacity:.85}
.badge.p4 i{background:#2f73c9;opacity:.85}

/* footer */
.footer{left:0;top:1066px;width:1103px;height:134px;background:var(--footer);color:var(--footer-text)}
.footer h5{position:absolute;left:215px;top:20px;font-family:"Ubuntu",sans-serif;font-size:13px;font-weight:500;color:#fff}
.contact-line{position:absolute;left:214px;top:46px;font-size:9.5px;display:flex;gap:16px;white-space:nowrap}
.contact-rule{position:absolute;left:214px;top:64px;width:518px;height:1px;background:#666}
.foot-nav{position:absolute;left:215px;top:76px;font-size:9.5px;display:flex;gap:12px}
.side-social{position:absolute;left:790px;top:18px;list-style:none;font-size:9.5px;line-height:17.5px}
.side-social li{display:flex;gap:10px;align-items:center}
.side-social i{display:inline-block;width:6px;height:6px;background:#bbb;border-radius:50%}
.copyright-rule{position:absolute;left:70px;top:108px;width:963px;height:1px;background:#5c5c5c}
.copyright{position:absolute;left:215px;top:117px;font-size:9.5px}
</style>
</head>
<body>

<header>
  <nav class="abs social-top"><span>Facepage</span><span>Chirper</span><span>WorkLink</span><span>SearchPlus</span></nav>
  <div class="abs brand"><span class="brand-mark"></span><span class="brand-name">MarshSmile Dental</span></div>
  <div class="abs chat">
    <div class="abs chat-avatar" role="img" aria-label="Illustration of a receptionist with headset"></div>
    <div class="abs chat-q">Have Questions?</div>
    <div class="abs chat-btn"><small>Click Here to:</small><span>Chat Online</span></div>
  </div>
  <div class="abs enquiries">
    <h4><svg width="11" height="11" viewBox="0 0 12 12"><path d="M2 1l3 3-1.5 1.5a7 7 0 003 3L8 7l3 3-2 2C5 12 0 7 0 3z" fill="#3f7ac5"/></svg>ENQUIRIES</h4>
    <p>Call: 111 555 20</p>
    <p>Intl: +12 3 555 0148</p>
  </div>
  <nav class="abs nav">
    <a class="active">HOME</a><a>ABOUT US</a><a>THE PRACTICE</a><a>ARE OF EXPERTIESE</a><a>APPOINTMENT</a><a>CONTACT</a>
  </nav>
</header>

<section>
  <div class="abs hero"></div>
  <div class="abs hero-window"></div>
  <div class="abs hero-photo" role="img" aria-label="Photo of a smiling family: mother, father and young daughter"></div>
  <div class="abs hero-copy">
    <div class="lead">We Care About</div>
    <div class="title">PROIN GRAVIDA NIBH</div>
    <div class="sub">lorem quis bibendum auctor, nisi elit</div>
  </div>
</section>

<section class="abs appt">
  <div class="abs tab main">Make an Appointment</div>
  <div class="abs tab emergency">
    <svg width="17" height="15" viewBox="0 0 18 16"><rect x="0" y="3" width="18" height="13" rx="2" fill="#3f7ac5"/><rect x="6" y="0" width="6" height="4" rx="1" fill="none" stroke="#3f7ac5" stroke-width="1.5"/><circle cx="9" cy="9.5" r="4" fill="#fff"/><path d="M9 7.3v4.4M6.8 9.5h4.4" stroke="#3f7ac5" stroke-width="1.5"/></svg>
    For Emergency Cases
  </div>

  <div class="abs col hours">
    <h3><svg width="15" height="15" viewBox="0 0 16 16"><circle cx="8" cy="8" r="6.5" fill="none" stroke="#fff" stroke-width="2"/><path d="M8 4v4h3" stroke="#fff" stroke-width="1.6" fill="none"/></svg>Working Time</h3>
    <ul>
      <li><span>Monday – Friday</span><span>8.00 – 17.00</span></li>
      <li><span>Saturday</span><span>9.30 – 17.30</span></li>
      <li><span>Sunday</span><span>9.30 – 15.00</span></li>
    </ul>
  </div>

  <div class="abs col timetable">
    <h3><svg width="15" height="15" viewBox="0 0 16 16"><rect x="1" y="2" width="14" height="13" fill="none" stroke="#fff" stroke-width="1.5"/><path d="M1 5.5h14M4 0v4M12 0v4M4 8h2M7 8h2M10 8h2M4 11h2M7 11h2M10 11h2" stroke="#fff" stroke-width="1.3"/></svg>Doctors Timetable</h3>
    <p>Lorem ipsum dolor sit amet, consectetur adipisicing elit, sed do eiusmod tempor incididunt ut labore et dolore.</p>
    <span class="btn" style="left:47px;top:102px;width:89px">View Timetable</span>
  </div>

  <div class="abs col booking">
    <h3><svg width="15" height="15" viewBox="0 0 16 16"><rect x="1" y="2" width="14" height="13" fill="none" stroke="#fff" stroke-width="1.5"/><path d="M1 5.5h14M4 0v4M12 0v4M4 8h2M7 8h2M10 8h2M4 11h2M7 11h2M10 11h2" stroke="#fff" stroke-width="1.3"/></svg>Booking a Visit</h3>
    <span class="field" style="left:0;top:33px">Select Department</span>
    <span class="field" style="left:138px;top:33px">Your Phone</span>
    <span class="field" style="left:0;top:68px">Full Name</span>
    <span class="field" style="left:138px;top:68px">mm/dd/yyyy</span>
    <span class="btn" style="left:170px;top:102px;width:89px">Send</span>
  </div>
</section>

<section>
  <h2 class="abs section-title">About <b>OUR SERVICES</b></h2>
  <div class="abs section-rule"></div>
  <div class="abs section-accent"></div>
  <div class="abs cards">
    <article class="card c1">
      <div class="card-photo cosmetic" role="img" aria-label="Photo of a smiling young woman"></div>
      <svg class="plus" viewBox="0 0 12 12"><path d="M6 2.5v7M2.5 6h7" stroke="#fff" stroke-width="2"/></svg>
      <div class="card-body"><h4><b>Cosmetic</b> Dentistry</h4><p>Lorem Ipsum. Proin gravida nibh vel velit auctor aliquet. Aenean sollicitudin, lorem quis bibendum auctor, nisi elit consequat ipsum,</p></div>
      <div class="more">Read more →</div>
    </article>
    <article class="card c2">
      <div class="card-photo whiten" role="img" aria-label="Photo of a smile with a dental mirror"></div>
      <svg class="plus" viewBox="0 0 12 12"><path d="M6 2.5v7M2.5 6h7" stroke="#fff" stroke-width="2"/></svg>
      <div class="card-body"><h4><b>Tooth</b> Whitening</h4><p>Lorem Ipsum. Proin gravida nibh vel velit auctor aliquet. Aenean sollicitudin, lorem quis bibendum auctor, nisi elit consequat ipsum,</p></div>
      <div class="more">Read more →</div>
    </article>
    <article class="card c3">
      <div class="card-photo smile" role="img" aria-label="Close-up photo of white teeth and lips"></div>
      <svg class="plus" viewBox="0 0 12 12"><path d="M6 2.5v7M2.5 6h7" stroke="#fff" stroke-width="2"/></svg>
      <div class="card-body"><h4><b>Smile</b> Makeover</h4><p>Lorem Ipsum. Proin gravida nibh vel velit auctor aliquet. Aenean sollicitudin, lorem quis bibendum auctor, nisi elit consequat ipsum,</p></div>
      <div class="more">Read more →</div>
    </article>
    <article class="card c4">
      <div class="card-photo implant" role="img" aria-label="Photo of a dental implant model"></div>
      <svg class="plus" viewBox="0 0 12 12"><path d="M6 2.5v7M2.5 6h7" stroke="#fff" stroke-width="2"/></svg>
      <div class="card-body"><h4><b>Dental</b> Implants</h4><p>Lorem Ipsum. Proin gravida nibh vel velit auctor aliquet. Aenean sollicitudin, lorem quis bibendum auctor, nisi elit consequat ipsum,</p></div>
      <div class="more">Read more →</div>
    </article>
  </div>
</section>

<section>
  <div class="abs band"></div>
  <div class="abs partners">
    <span class="arrow"><svg width="8" height="10" viewBox="0 0 8 10"><path d="M6 1L2 5l4 4" stroke="#fff" stroke-width="2" fill="none"/></svg></span>
    <span class="badge p1" role="img" aria-label="Partner badge"><i></i></span>
    <span class="badge p2" role="img" aria-label="Partner badge"><i></i></span>
    <span class="badge p3" role="img" aria-label="Partner badge"><i></i></span>
    <span class="badge p4" role="img" aria-label="Partner badge"><i></i></span>
    <span class="arrow"><svg width="8" height="10" viewBox="0 0 8 10"><path d="M2 1l4 4-4 4" stroke="#fff" stroke-width="2" fill="none"/></svg></span>
  </div>
</section>

<footer class="abs footer">
  <h5>Contact Information</h5>
  <div class="contact-line">
    <span>⌂ Proin gravida nibh vel velit auctor aliquet, UK.</span>
    <span>✆ Email: info@marshsmile.example</span>
    <span>✉ Email: info@marshsmile.example</span>
  </div>
  <div class="contact-rule"></div>
  <nav class="foot-nav"><span>Home</span><span>|</span><span>About Us</span><span>|</span><span>The Practice</span><span>|</span><span>Area of Expertise</span><span>|</span><span>Appointment</span><span>|</span><span>Contact</span></nav>
  <ul class="side-social">
    <li><i></i>Facepage</li><li><i></i>Chirper</li><li><i></i>WorkLink</li><li><i></i>SearchPlus</li><li><i></i>RSS Feeds</li>
  </ul>
  <div class="copyright-rule"></div>
  <div class="copyright">© Copyright Dr. Colin Marsh 2014</div>
</footer>

</body>
</html>
```